Body therapist needs a business card

I need a card for my business which is teaching trainings in body therapy, the company is called Wexcombe Educational Group. I teach to massage therapists around Australia, South East Asia and the USA. I am attaching my logo which will guide you as to what colours I would like to have you consider. Please consult my website to find out more about what I do. www.corvantela.com.au

My name is Daniel Wexcombe. My phone number is (03) 9417 2608 or 0461753208. email is info@corvantela.com.au

```html
<!DOCTYPE html>
<html lang="en">
<head>
<meta charset="utf-8">
<title>Wexcombe Educational Group – Business Card</title>
<link href="https://fonts.googleapis.com/css2?family=Roboto:wght@400;500;700&display=swap" rel="stylesheet">
<style>
  :root {
    --backdrop: #1d1d1d;
    --card: #2c2c2c;
    --card-edge: #333333;
    --emboss: #7c7c7c;
    --emboss-dot: #3a3a3a;
    --white: #f2f2f2;
    --lime: #c6d92b;
    --rule: #9a9a9a;
  }
  * { box-sizing: border-box; margin: 0; padding: 0; }
  html, body {
    width: 1200px; height: 901px; overflow: hidden;
    background: var(--backdrop);
    font-family: "Roboto", Arial, sans-serif;
  }
  .canvas {
    position: relative; width: 1200px; height: 901px;
    display: flex; flex-direction: column; align-items: center;
    justify-content: center; gap: 30px;
  }
  .card {
    position: relative; width: 700px; height: 400px;
    background: var(--card);
    border: 1px solid var(--card-edge);
    box-shadow: 0 10px 30px rgba(0,0,0,0.5);
  }
  /* front */
  .card--front { display: flex; align-items: center; justify-content: center; }
  .brand { display: flex; align-items: center; gap: 22px; }
  .brand__dot { border-radius: 50%; flex: none; }
  .brand__name { font-weight: 400; line-height: 1.1; }
  .card--front .brand__dot { width: 120px; height: 120px; background: var(--emboss-dot); }
  .card--front .brand__name { color: var(--emboss); font-size: 40px; width: 300px; }

  /* back */
  .card--back { display: flex; align-items: center; padding: 0 40px 0 50px; }
  .card--back .brand { width: 270px; gap: 16px; }
  .card--back .brand__dot { width: 60px; height: 60px; background: var(--lime); }
  .card--back .brand__name { color: var(--white); font-size: 24px; width: 190px; }
  .divider { width: 1px; height: 220px; background: var(--rule); margin: 0 30px 0 20px; }
  .contact { color: var(--white); }
  .contact__name { color: var(--lime); font-weight: 700; font-size: 26px; margin-bottom: 14px; }
  .contact__address { font-size: 18px; line-height: 1.25; margin-bottom: 16px; }
  .contact__list { list-style: none; font-size: 19px; }
  .contact__item { display: flex; align-items: center; gap: 12px; margin-bottom: 8px; }
  .contact__icon { width: 18px; height: 18px; flex: none; fill: var(--lime); }
</style>
</head>
<body>
<main class="canvas">
  <section class="card card--front">
    <div class="brand">
      <span class="brand__dot"></span>
      <span class="brand__name">Wexcombe Educational Group</span>
    </div>
  </section>

  <section class="card card--back">
    <div class="brand">
      <span class="brand__dot"></span>
      <span class="brand__name">Wexcombe Educational Group</span>
    </div>
    <span class="divider"></span>
    <div class="contact">
      <h1 class="contact__name">Daniel Wexcombe</h1>
      <p class="contact__address">P.O. Box 2784, Elmridge North<br>Australia, Victoria, 3174</p>
      <ul class="contact__list">
        <li class="contact__item">
          <svg class="contact__icon" viewBox="0 0 24 24" aria-hidden="true"><path d="M6.6 10.8a15 15 0 0 0 6.6 6.6l2.2-2.2a1 1 0 0 1 1-.25 11.4 11.4 0 0 0 3.6.57 1 1 0 0 1 1 1V20a1 1 0 0 1-1 1A17 17 0 0 1 3 4a1 1 0 0 1 1-1h3.5a1 1 0 0 1 1 1c0 1.25.2 2.45.57 3.57a1 1 0 0 1-.25 1z"/></svg>
          (03) 9417 2608
        </li>
        <li class="contact__item">
          <svg class="contact__icon" viewBox="0 0 24 24" aria-hidden="true"><path d="M2 5h20v14H2z M4 7v.4l8 5.2 8-5.2V7z" fill-rule="evenodd"/></svg>
          info@corvantela.com.au
        </li>
        <li class="contact__item">
          <svg class="contact__icon" viewBox="0 0 24 24" aria-hidden="true"><path d="M12 2a10 10 0 1 0 0 20 10 10 0 0 0 0-20zm0 2a8 8 0 0 1 7.7 6h-4.2A13 13 0 0 0 13 4.1 8 8 0 0 1 12 4zm-1 .1A13 13 0 0 0 8.5 10H4.3A8 8 0 0 1 11 4.1zM4.3 14h4.2A13 13 0 0 0 11 19.9 8 8 0 0 1 4.3 14zm8.7 5.9a13 13 0 0 0 2.5-5.9h4.2a8 8 0 0 1-6.7 5.9zM10.5 10h3a11 11 0 0 1 0 4h-3a11 11 0 0 1 0-4z"/></svg>
          www.corvantela.com.au
        </li>
      </ul>
    </div>
  </section>
</main>
</body>
</html>
```